Bright Years Forward an age management group needs a modern looking website developed asap

Bright Years Forward is an age management group lead by a board certified medical doctor (who also specializes in age management medicine) and a 7th degree black belt jiu-jitsu master. Both have joined forces to create a unique doctor supervised anti-aging medical, nutritional, hormonal, exercise protocol never seen before.
This marriage between medicine and athleticism will create the worlds first complete anti-aging program designed for anyone wishing to remain as healthy and as young for as long as possible.

Our Mission and Vision: "To provide clients cutting edge anti aging programs and protocols designed to "turn-back-the-clock-one-second-at-a-time. Let's all Bright Years Forward..together!"

Bright Years Forward's program consists of 6 unique tiers/platforms each encompassing a specific need.
The 6 tiers are:
1. Apex Care: A medical doctor supervised unique and proprietary hormone optimization program and protocol developed by a board certified medical doctor trained by Volarix ( a world leader in age management medicine) who has practiced age management medicine for the past 7 years
2. Apex Slim: A medical doctor supervised unique and proprietary weight management program and protocol developed by a published medical doctor who's diet book "Fresh start: Shed those pounds soon" was just launched
3.Apex Motion: A master athlete supervised training program and protocol, with access to a large proprietary exercise video databank developed by a 7th degree black belt jiu-jitsu master.
4. Apex Plate: A chef driven and supervised home delivered healthy meals. Each meal is made from scratch, and is specifically tailored and targeted according to each patient's specific needs.
5. ApexDailyMix: A doctor formulated-master athlete approved most complete multi vitamin-mineral-anti-oxidant and supplement pack available on the market today. ApexDailyMix is: made in the USA, and QSA approved vitamin factory, gluten free, sugar free, and artificial color free.
6. Apex Academy: A unique CME approved teaching workshop intended for those physicians who lack expertise in age management but want to become proficient in the art of hormone optimization and age management medicine. The 2-day workshop is held twice monthly on Saturday and Sunday in sunny Florida.

This is our scope and goal.
We want to become the leaders in age management medicine by being the first to unite doctors-athletes-chefs-nutritionist together in an effort to deliver the most advanced most cutting edge programs and protocols so we may all : BRIGHT YAERS FORWARD!

We already have the logo for Bright years forward.
Please keep in mind the following:
1. Apex care should be in green and black
2. Apex slim should be in purple and black
3. Apex motion in orange and black
4. Apx plate in yellow and black
5. ApexDialyMix in red and black
6. Apex academy in gray and black

Target Market(s)

Adults Males and females wishing to remain as healthy and as young for as long as possible
Obese and overweight adults males and females
Athletes males and females
Young obese and overweight males and females
ALL can be from any country!

Industry/Entity Type

Health And Wellness

Coding

Coded - Design and coding required

Number of Pages Required

5+ page

Requirements
Must have
• The front page must have our mission statement as well as the 6 tiers/platforms displayed (Apex Care, Apex Slim, Apex Motion, Apex Plate, ApexDailyMix, Apex Academy) and each platform when "cliked on" should open up in its own unique page.
• The capability for clients to log on to any of the pages using assigned usernames and passwords.
• The capability of check out (credit cards, paypal) from any of the pages. EX the client may want to buy ApexDailyMix. He/She would click on the main page then click on ApexDailymix page and choose to buy the vitamin. Same For the rest: He/she may want to buy the weight loss program (apex slim), or the Hormone program (apex care) or the food delivered home (apex Plate) or apex motion (access to the exercise video databank) or attend the workshop (buy the teaching program..BUT this will ONLY be accessible if the client is a medical doctor and has a valid medical license).
• Also the client may want to have full access to ALL the 6 tiers, thus on the FRONT page we need a checkout with "full access to tiers"
• Also we need to make sure no videos are downloade but only viewed. we need to have this safety built in.
• Also we nee to be able to keep track of emails and have stats. and any email inquiry must be diverted to my iphone.
Nice to have
• Modern look with pop-ups and graphics and iphone and android capability
Should not have
• nothing explicit

```html
<!DOCTYPE html>
<html lang="en">
<head>
<meta charset="utf-8">
<title>Bright Years Forward</title>
<link href="https://fonts.googleapis.com/css2?family=Lato:wght@400;700&family=Raleway:wght@400;500;600;700&display=swap" rel="stylesheet">
<style>
:root{
  --sky:#4bb8d6;
  --ink:#1a1a1a;
  --green:#8dc63f;
  --purple:#6b51a0;
  --orange:#f39130;
  --yellow:#e2d11c;
  --red:#d2232a;
  --gray:#8c8c8c;
  --paper:#ffffff;
  --mist:#f4f4f4;
  --footer:#2b2b2b;
  --muted:#8a8a8a;
  --brand-blue:#3fa9d2;
}
*{box-sizing:border-box;margin:0;padding:0}
html,body{width:1200px;height:2791px;overflow:hidden}
body{position:relative;background:var(--paper);font-family:'Lato',sans-serif;color:var(--ink)}
.abs{position:absolute}

/* header */
.site-header{left:0;top:0;width:1200px;height:141px;background:#f8f7f8}
.brand{left:117px;top:22px;display:flex;align-items:center;gap:14px}
.brand-dot{width:70px;height:70px;border-radius:50%;background:var(--green)}
.brand-name{font-family:'Raleway',sans-serif;font-weight:600;font-size:22px;color:var(--brand-blue)}
.login-btn{left:958px;top:68px;width:117px;height:37px;border:2px solid #bdbdbd;font-family:'Lato',sans-serif;font-size:12px;color:#333;display:flex;align-items:center;justify-content:center;background:#fff}

.main-nav{left:0;top:141px;width:1200px;height:53px;background:var(--sky);display:flex;align-items:center;padding-left:113px;gap:36px}
.main-nav span{font-family:'Raleway',sans-serif;font-size:13px;font-weight:500;color:#fff;text-transform:uppercase}

/* hero */
.hero{left:0;top:194px;width:1200px;height:511px;background:linear-gradient(90deg,#f4f4f4 0%,#ededed 45%,#e2e2e2 100%);overflow:hidden}
.hero-photo{left:586px;top:0;width:614px;height:511px;background:linear-gradient(120deg,#dfe7e9 0%,#3fb8a7 30%,#2fa89a 60%,#c9a48c 85%,#e9e9e9 100%)}
.hero-lead{left:95px;top:80px;width:540px;text-align:center;font-size:20px;line-height:30px;color:#222}
.hero-ribbon{left:0;top:158px}
.hero-slogan{left:100px;top:171px;width:520px;text-align:center;font-size:26px;line-height:32px;color:#fff;font-family:'Lato',sans-serif}
.hero-tag{left:95px;top:257px;width:540px;text-align:center;font-size:22px;font-weight:700;color:#222}
.hero-cta{left:294px;top:333px;width:192px;height:40px;border:3px solid #6b8f3a;color:#6b8f3a;font-family:'Raleway',sans-serif;font-weight:700;font-size:19px;letter-spacing:.5px;display:flex;align-items:center;justify-content:center}
.hero-arrow{top:204px}

/* tiers */
.tier{width:270px}
.tier-head{height:57px;display:flex;align-items:center;justify-content:center;font-family:'Raleway',sans-serif;font-weight:700;font-size:21px;color:#fff;text-transform:uppercase;letter-spacing:.3px}
.tier-image{height:183px}
.tier-copy{height:163px;background:var(--ink);color:#e8e8e8;font-size:12px;line-height:20.5px;padding:20px 22px 0 30px}
.tier-more{width:115px;height:30px;margin:17px auto 0;border:2px solid #d6d6d6;font-family:'Raleway',sans-serif;font-size:10px;color:#999;display:flex;align-items:center;justify-content:center;letter-spacing:.5px}
.care .tier-head{background:var(--green)}
.slim .tier-head{background:var(--purple)}
.motion .tier-head{background:var(--orange)}
.plate .tier-head{background:var(--yellow)}
.mix .tier-head{background:var(--red)}
.academy .tier-head{background:var(--gray)}

/* videos */
.videos{left:0;top:1767px;width:1200px;height:438px;background:var(--mist)}
.section-title{font-family:'Raleway',sans-serif;font-weight:600;font-size:30px;text-align:center;width:1200px;left:0}
.video-card{top:131px;width:317px;height:229px;background:#fff;padding:10px;box-shadow:0 2px 6px rgba(0,0,0,.12)}
.video-thumb{position:relative;width:100%;height:100%}
.play{position:absolute;left:50%;top:50%;transform:translate(-50%,-50%)}

/* newsletter */
.newsletter{left:0;top:2205px;width:1200px;height:344px;background:var(--sky)}
.newsletter .section-title{color:#fff;top:40px;font-size:32px}
.field{left:420px;width:348px;height:47px;background:#fff;font-size:12px;color:#777;padding-left:16px;display:flex;align-items:center}
.signup{left:534px;top:256px;width:138px;height:47px;background:#111;color:#fff;font-family:'Raleway',sans-serif;font-weight:700;font-size:13px;display:flex;align-items:center;justify-content:center}

/* footer */
.site-footer{left:0;top:2549px;width:1200px;height:242px;background:var(--footer)}
.foot-head{font-family:'Raleway',sans-serif;font-weight:700;font-size:12px;color:#fff;text-transform:uppercase;top:36px}
.foot-text{font-size:11px;line-height:18.5px;color:var(--muted)}
.pay-row{left:132px;top:152px;display:flex;gap:12px}
.pay-row span{width:41px;height:27px;border-radius:3px;background:#d9d9d9;display:block}
.social{left:862px;top:2643px;display:flex;gap:10px}
.social span{width:30px;height:30px;border-radius:50%;background:#8d8d8d;display:block}
.copyright{left:862px;top:2694px;font-size:12px;color:#ddd}
</style>
</head>
<body>

<header class="site-header abs">
  <div class="brand abs"><span class="brand-dot"></span><span class="brand-name">Bright Years Forward</span></div>
  <div class="login-btn abs">USER LOGIN</div>
</header>

<nav class="main-nav abs">
  <span>Home</span><span>Apex Care</span><span>Apex Slim</span><span>Apex Motion</span><span>Apex Plate</span><span>ApexDailyMix</span><span>Apex Academy</span>
</nav>

<section class="hero abs">
  <div class="hero-photo abs" role="img" aria-label="Doctor in teal scrubs holding a stethoscope, arms crossed"></div>
  <p class="hero-lead abs">To provide clients cutting edge anti aging programs and protocols designed to</p>
  <svg class="hero-ribbon abs" width="640" height="90" viewBox="0 0 640 90"><polygon points="0,0 640,0 600,90 0,90" fill="#8dc63f"/></svg>
  <p class="hero-slogan abs">TURN-BACK-THE-CLOCK-ONE-SEOND<br>AT-A-TIME</p>
  <p class="hero-tag abs">Let's all Bright Years Forward..together!</p>
  <div class="hero-cta abs">LEARN MORE</div>
  <svg class="hero-arrow abs" style="left:18px" width="48" height="48" viewBox="0 0 48 48"><circle cx="24" cy="24" r="21" fill="none" stroke="#222" stroke-width="2.5"/><polyline points="28,14 18,24 28,34" fill="none" stroke="#222" stroke-width="2.5"/></svg>
  <svg class="hero-arrow abs" style="left:1124px" width="48" height="48" viewBox="0 0 48 48"><circle cx="24" cy="24" r="21" fill="none" stroke="#222" stroke-width="2.5"/><polyline points="20,14 30,24 20,34" fill="none" stroke="#222" stroke-width="2.5"/></svg>
</section>

<article class="tier care abs" style="left:140px;top:765px">
  <div class="tier-head">Apex Care</div>
  <div class="tier-image" role="img" aria-label="Doctor holding a red heart beside a stethoscope" style="background:linear-gradient(135deg,#f2f4f6,#dfe4ea 60%,#e9c9c9)"></div>
  <div class="tier-copy">A medical doctor supervised unique and proprietary hormone optimiza-tion program and protocol devel-oped by a board certified medical doctor trained by Volarix ....</div>
  <div class="tier-more">READ MORE</div>
</article>
<article class="tier slim abs" style="left:461px;top:765px">
  <div class="tier-head">Apex Slim</div>
  <div class="tier-image" role="img" aria-label="Smiling doctor in a white coat holding a clipboard" style="background:linear-gradient(135deg,#cfe3f2,#e9eef2 55%,#bcd2e4)"></div>
  <div class="tier-copy">A medical doctor supervised unique and proprietary weight management program and protocol developed by a published medical doctor who's diet ....</div>
  <div class="tier-more">READ MORE</div>
</article>
<article class="tier motion abs" style="left:783px;top:765px">
  <div class="tier-head">Apex Motion</div>
  <div class="tier-image" role="img" aria-label="Trainer guiding a client on a gym exercise machine" style="background:linear-gradient(135deg,#e7e2dc,#c9bfb4 55%,#efece8)"></div>
  <div class="tier-copy">A master athlete supervised training program and protocol, with access to a large proprietary exercise video databank developed by a 7th degree black belt jiu-jitsu master.</div>
  <div class="tier-more">READ MORE</div>
</article>

<article class="tier plate abs" style="left:140px;top:1260px">
  <div class="tier-head">Apex Plate</div>
  <div class="tier-image" role="img" aria-label="Fresh fruit and vegetables with a measuring tape beside a doctor" style="background:linear-gradient(135deg,#e6f0dc,#e9b94c 45%,#d8623c 70%,#f1f1f1)"></div>
  <div class="tier-copy">A chef driven and supervised home delivered healthy meals. Each meal is made from scratch, and is specifi-cally tailored and targeted accord-ing to each patient's specific needs.</div>
  <div class="tier-more">READ MORE</div>
</article>
<article class="tier mix abs" style="left:461px;top:1260px">
  <div class="tier-head">ApexDailyMix</div>
  <div class="tier-image" role="img" aria-label="Doctor holding a handful of vitamin capsules" style="background:linear-gradient(180deg,#f3f3f3,#e3e6ea 60%,#b9cde0)"></div>
  <div class="tier-copy">A doctor formulated-master athlete approved most complete multi vita-min-mineral-anti-oxidant and sup-plement pack available on the market today. ApexDailyMix is:</div>
  <div class="tier-more">READ MORE</div>
</article>
<article class="tier academy abs" style="left:783px;top:1260px">
  <div class="tier-head">Apex Academy</div>
  <div class="tier-image" role="img" aria-label="Medical staff attending a workshop presentation" style="background:linear-gradient(135deg,#eef2f5,#c7d6e2 50%,#6f8fb3)"></div>
  <div class="tier-copy">A unique CME approved teaching workshop intended for those physi-cians who lack expertise in age management but want to become proficient in the art of hormone</div>
  <div class="tier-more">READ MORE</div>
</article>

<section class="videos abs">
  <h2 class="section-title abs" style="top:40px">OUR LATEST VIDEOS</h2>
  <div class="video-card abs" style="left:106px">
    <div class="video-thumb" role="img" aria-label="Family standing with a group in a clinic hallway" style="background:linear-gradient(135deg,#d9dde2,#aebccb 55%,#e6e8ea)">
      <svg class="play" width="64" height="64" viewBox="0 0 64 64"><circle cx="32" cy="32" r="29" fill="#fff" stroke="#555" stroke-width="3"/><circle cx="32" cy="32" r="23" fill="#6b6b6b"/><polygon points="26,20 46,32 26,44" fill="#fff"/></svg>
    </div>
  </div>
  <div class="video-card abs" style="left:439px">
    <div class="video-thumb" role="img" aria-label="Caregiver embracing an older woman outdoors" style="background:linear-gradient(135deg,#e9dccb,#b7c98e 50%,#6c9bc8)">
      <svg class="play" width="64" height="64" viewBox="0 0 64 64"><circle cx="32" cy="32" r="29" fill="#fff" stroke="#555" stroke-width="3"/><circle cx="32" cy="32" r="23" fill="#6b6b6b"/><polygon points="26,20 46,32 26,44" fill="#fff"/></svg>
    </div>
  </div>
  <div class="video-card abs" style="left:770px">
    <div class="video-thumb" role="img" aria-label="Doctor and nurse visiting a patient in a hospital bed" style="background:linear-gradient(135deg,#e4eaee,#9fbcd3 55%,#dfe5ea)">
      <svg class="play" width="64" height="64" viewBox="0 0 64 64"><circle cx="32" cy="32" r="29" fill="#fff" stroke="#555" stroke-width="3"/><circle cx="32" cy="32" r="23" fill="#6b6b6b"/><polygon points="26,20 46,32 26,44" fill="#fff"/></svg>
    </div>
  </div>
</section>

<section class="newsletter abs">
  <h2 class="section-title abs">STAY IN TOUCH&nbsp; WITH US</h2>
  <div class="field abs" style="top:124px">Enter First Name</div>
  <div class="field abs" style="top:184px">Enter Email Address</div>
  <div class="signup abs">SIGN UP</div>
</section>

<footer class="site-footer abs">
  <h3 class="foot-head abs" style="left:132px">Contact Us</h3>
  <p class="foot-text abs" style="left:132px;top:76px">18 Avenue Meridian<br>Next to Valemart, Near Harbor Bank<br>Riverside, Port Elan.</p>
  <div class="pay-row abs"><span></span><span></span><span></span><span></span><span></span></div>
  <h3 class="foot-head abs" style="left:527px">Information</h3>
  <p class="foot-text abs" style="left:527px;top:76px;line-height:20.5px">Apex Care<br>Apex Slim<br>Apex Motion<br>Apex Plate<br>ApexDailyMix<br>Apex Academy</p>
</footer>
<div class="social abs"><span></span><span></span><span></span><span></span><span></span></div>
<p class="copyright abs">Copyright @ 2016. All rights reserved</p>

</body>
</html>
```